Need updated stationery design for chiropractic clinic

We recently moved our office and are looking to refresh our letterhead, business cards, presentation folder and envelopes. I tend to prefer simple, clean designs. We communicate with a lot of attorneys and want to exude professionalism. I have attached our logo and 2 additional versions (all white and white letters instead of grey).

Target Market(s)

Other medical professionals and attorneys. Business cards will go to patients as well.

Industry/Entity Type

Healthcare

```html
<!DOCTYPE html>
<html lang="en">
<head>
<meta charset="utf-8">
<title>SpineWell Stationery</title>
<link href="https://fonts.googleapis.com/css2?family=Outfit:wght@300;400;500;600;700;800&display=swap" rel="stylesheet">
<style>
:root{
  --bg:#1b2838;
  --bg-light:#24364a;
  --blue:#0a97d0;
  --blue-deep:#0b5f97;
  --navy:#0d5c92;
  --teal:#06cdd4;
  --ink:#2b3440;
  --muted:#6b7682;
  --rule:#c9d3dc;
  --paper:#ffffff;
  --paper-tint:#f4f7fa;
}
*{margin:0;padding:0;box-sizing:border-box}
html,body{width:1200px;height:1097px;overflow:hidden}
body{
  font-family:"Outfit",sans-serif;color:var(--ink);
  background:radial-gradient(ellipse at 50% 20%,var(--bg-light),var(--bg) 70%);
  position:relative;
}
.label{position:absolute;font-size:10px;font-weight:500;letter-spacing:.3px;color:#c3ccd6}
.sheet{position:absolute;background:var(--paper);overflow:hidden;box-shadow:0 6px 18px rgba(0,0,0,.35)}
.abs{position:absolute}
.brand{position:absolute;display:flex;align-items:center;gap:4px;font-weight:600;color:var(--teal);white-space:nowrap;line-height:1}
.brand .mark{background:var(--teal);flex:none}
.brand.on-blue{color:#fff}
.brand.on-blue .mark{background:#fff}
.band{position:absolute;left:0;right:0;bottom:0}
.band .teal{position:absolute;left:0;bottom:0;height:45%;width:100%;background:var(--teal)}
.band .navy{position:absolute;right:0;bottom:0;height:100%;background:var(--navy);
  clip-path:polygon(6% 0,100% 0,100% 100%,0 100%);color:#fff;font-weight:600;display:flex;align-items:center;justify-content:center}
.contact{position:absolute;font-size:5.6px;line-height:8px;color:var(--ink);white-space:nowrap}
.contact svg{width:5px;height:5px;vertical-align:-0.5px;margin-right:3px}
.ico{fill:var(--teal)}
.letter p{font-size:5.3px;line-height:8.8px;color:var(--muted);text-align:justify;margin-bottom:8.8px}
.inv-table{position:absolute;left:22px;top:137px;width:294px;border-collapse:collapse;font-size:6.2px}
.inv-table th{background:#eef2f6;font-weight:600;text-align:left;height:16px;border-top:1px solid var(--rule);border-bottom:1px solid var(--rule)}
.inv-table td{height:30px;border-bottom:1px solid var(--rule)}
.inv-table td.t{font-weight:600}
.inv-small{position:absolute;font-size:5.8px;line-height:9.4px}
.notepad-lines{position:absolute;left:14px;right:14px;top:26px}
.notepad-lines div{height:11.1px;border-bottom:.6px solid #d3dae1}
</style>
</head>
<body>

<div class="label" style="left:56px;top:34px">LETTERHEAD</div>
<div class="label" style="left:432px;top:34px">FOLDER</div>
<div class="label" style="left:56px;top:546px">INVOICE</div>
<div class="label" style="left:430px;top:546px">BUSINESS CARD</div>
<div class="label" style="left:803px;top:546px">NOTEPAD</div>
<div class="label" style="left:430px;top:655px">ENVELOP</div>

<!-- LETTERHEAD -->
<section class="sheet letter" style="left:56px;top:54px;width:337px;height:472px">
  <div class="brand" style="left:23px;top:27px;font-size:15px"><span class="mark" style="width:12px;height:12px"></span>SpineWell</div>
  <div class="abs" style="right:31px;top:86px;font-size:5.6px;color:var(--muted)"><b style="color:var(--ink);font-weight:600">Date:</b> December 25, 2022</div>
  <div class="abs" style="left:32px;top:103px;font-size:5.8px;font-weight:600">Dear Sir,</div>
  <div class="abs" style="left:32px;top:120px;width:274px">
    <p>Lorem ipsum dolor sit amet, consectetur adipiscing elit, sed do eiusmod tempor incididunt ut labore et dolore magna aliqua. Diam volutpat commodo sed egestas. Nisi quis eleifend quam adipiscing vitae proin sagittis nisl. Nulla malesuada pellentesque elit eget gravida cum sociis natoque penatibus. Consequat semper viverra nam libero justo laoreet sit.</p>
    <p>Faucibus scelerisque eleifend donec pretium vulputate sapien. Dui nunc mattis enim ut tellus elementum. Suscipit adipiscing bibendum est ultricies integer quis auctor elit sed. Sit amet luctus venenatis lectus. Vestibulum sed arcu non odio euismod. Sagittis vitae et leo duis. Facilisi cras fermentum odio eu feugiat pretium nibh ipsum.</p>
    <p>Vestibulum lectus mauris ultrices eros in cursus turpis massa tincidunt. Sed faucibus turpis in eu. Cras tincidunt lobortis feugiat vivamus at. Nibh tortor id aliquet lectus proin. Nulla facilisi cras fermentum odio eu. Faucibus nisl tincidunt eget nullam non nisi est sit amet. Vitae congue mauris rhoncus aenean vel elit scelerisque mauris pellentesque. Id faucibus nisl tincidunt eget nullam non nisi est. Euismod in pellentesque massa placerat duis ultricies lacus sed. Tempus imperdiet nulla malesuada pellentesque elit eget gravida cum. Etiam erat velit scelerisque in dictum non consectetur a erat. Ipsum dolor sit amet consectetur adipiscing. Sit amet justo donec enim diam vulputate.</p>
    <p>Condimentum lacinia quis vel eros donec. Nibh cras pulvinar mattis nunc sed blandit libero volutpat. Ipsum a arcu cursus vitae congue. Etiam erat velit scelerisque in dictum non. Ut ornare lectus sit amet est placerat. Viverra maecenas accumsan lacus vel facilisis volutpat est velit egestas.</p>
    <p>Porta nibh venenatis cras sed felis eget. Dignissim cras tincidunt lobortis feugiat vivamus at augue eget arcu. Nulla porttitor massa id neque aliquam vestibulum.</p>
  </div>
  <div class="abs" role="img" aria-label="Handwritten signature" style="left:30px;top:344px;width:62px;height:18px;background:linear-gradient(90deg,#eef1f4,#f8f9fb)"></div>
  <div class="abs" style="left:31px;top:367px;font-size:7px;font-weight:600">Dana Mercer</div>
  <div class="abs" style="left:31px;top:376px;font-size:5.8px;color:var(--muted)">Director</div>
  <div class="contact" style="left:31px;top:416px">
    <div><svg viewBox="0 0 10 10"><path class="ico" d="M2 0l2 2-1 2c1 1 2 2 3 3l2-1 2 2-2 2C4 10 0 6 0 2z"/></svg>555 014 2290</div>
    <div><svg viewBox="0 0 10 10"><path class="ico" d="M0 2h10v6H0z"/></svg>hello@spinewell.com</div>
    <div style="margin-top:4px">1420 Orchard Ln</div>
    <div>Fairview California 95210</div>
  </div>
  <div class="band" style="height:19px"><div class="teal"></div><div class="navy" style="width:152px;font-size:5.6px">www.spinewell.com</div></div>
</section>

<!-- FOLDER -->
<section class="sheet" style="left:430px;top:54px;width:713px;height:475px">
  <div class="abs" style="left:0;top:0;width:357px;height:475px;background:linear-gradient(180deg,#0a9ad3,#0b93cc)"></div>
  <div class="brand on-blue" style="left:27px;top:425px;font-size:15px"><span class="mark" style="width:12px;height:12px"></span>SpineWell</div>
  <div class="abs" style="left:357px;top:0;width:356px;height:327px;background:linear-gradient(160deg,#079fd4,#0a93cc)"></div>
  <div class="abs" style="left:357px;top:311px;width:356px;height:16px;background:var(--blue-deep)"></div>
  <div class="abs" style="left:537px;top:304px;width:176px;height:23px;background:var(--teal);clip-path:polygon(12% 0,100% 0,100% 100%,0 100%)"></div>
  <div class="abs" style="left:399px;top:172px;font-size:25px;font-weight:800;line-height:22px;color:#fff">COMPANY<br>HEADLINE</div>
  <div class="abs" style="left:399px;top:230px;width:145px;font-size:5.6px;line-height:9.3px;color:#e4f4fb">Lorem ipsum dolor sit amet, consectet adipiscing elit sed do eiusmod tempor incididunt ut labore.</div>
  <div class="brand" style="left:399px;top:425px;font-size:15px"><span class="mark" style="width:12px;height:12px"></span>SpineWell</div>
  <div class="abs" style="right:24px;top:437px;font-size:5.6px;font-weight:600;color:var(--navy)">WWW.SPINEWELL.COM</div>
</section>

<!-- INVOICE -->
<section class="sheet" style="left:56px;top:566px;width:337px;height:472px">
  <div class="abs" style="left:0;top:0;width:191px;height:68px;background:#eef2f6;clip-path:polygon(0 0,100% 0,94% 100%,0 100%)"></div>
  <div class="abs" style="left:0;top:0;width:191px;height:59px;background:var(--navy);clip-path:polygon(0 0,100% 0,80% 100%,0 100%)"></div>
  <div class="abs" style="left:27px;top:24px;font-size:19px;font-weight:700;color:#fff">INVOICE</div>
  <div class="brand" style="left:213px;top:31px;font-size:15px"><span class="mark" style="width:12px;height:12px"></span>SpineWell</div>
  <div class="abs" style="left:22px;top:81px;font-size:6.5px">Invoice to:</div>
  <div class="abs" style="left:22px;top:93px;font-size:8.5px;font-weight:600">Dana Mercer</div>
  <div class="abs" style="left:22px;top:105px;font-size:5.6px;line-height:9px">1420 Orchard Ln<br>Fairview California 95210</div>
  <div class="abs" style="left:213px;top:81px;width:103px;font-size:6.5px;line-height:12.5px;display:grid;grid-template-columns:1fr auto">
    <span>Invoice#</span><span>52135</span><span>Date</span><span>15 / 12 / 2022</span>
  </div>
  <table class="inv-table">
    <thead><tr><th style="padding-left:11px;width:35px">SL.</th><th>Item Description</th><th style="width:49px">Price</th><th style="width:35px">Qty.</th><th style="width:39px">Total</th></tr></thead>
    <tbody>
      <tr><td style="padding-left:11px">1.</td><td>Lorem ipsum dolor sit egestas amet</td><td>$50.00</td><td>2</td><td class="t">$50.00</td></tr>
      <tr><td style="padding-left:11px">2.</td><td>Consectetur adipiscing elit</td><td>$20.00</td><td>1</td><td class="t">$20.00</td></tr>
      <tr><td style="padding-left:11px">3.</td><td>Sed do eiusmod tempor incididunt</td><td>$30.00</td><td>3</td><td class="t">$30.00</td></tr>
      <tr><td style="padding-left:11px">4.</td><td>Labore et dolore magna aliqua</td><td>$40.00</td><td>2</td><td class="t">$40.00</td></tr>
      <tr><td style="padding-left:11px">5.</td><td>Diam volutpat commodo sed egestas</td><td>$50.00</td><td>3</td><td class="t">$50.00</td></tr>
    </tbody>
  </table>
  <div class="abs" style="left:22px;top:334px;width:294px;border-top:1px solid var(--rule)"></div>
  <div class="abs" style="left:34px;top:349px;font-size:6.2px">Thank you for your business</div>
  <div class="abs" style="left:34px;top:371px;font-size:6.5px;font-weight:600">Payment Info:</div>
  <div class="inv-small" style="left:34px;top:381px">Account No:<br>A/C Name:<br>Bank Details:</div>
  <div class="inv-small" style="left:78px;top:381px">555 014 2290<br>Lorem Ipsum<br>Add your bank details</div>
  <div class="abs" style="left:217px;top:349px;font-size:6.2px;line-height:12.5px">Sub Total:<br>Tax:</div>
  <div class="abs" style="left:277px;top:349px;font-size:6.2px;line-height:12.5px;font-weight:600">$250.00<br>0.00%</div>
  <div class="abs" style="left:192px;top:377px;width:124px;border-top:1px solid var(--rule)"></div>
  <div class="abs" style="left:217px;top:383px;font-size:7.5px">Total:</div>
  <div class="abs" style="left:277px;top:382px;font-size:8px;font-weight:600">$250.00</div>
  <div class="contact" style="left:34px;top:428px"><div>1420 Orchard Ln</div><div>Fairview California 95210</div></div>
  <div class="contact" style="left:217px;top:428px">
    <div><svg viewBox="0 0 10 10"><path class="ico" d="M2 0l2 2-1 2c1 1 2 2 3 3l2-1 2 2-2 2C4 10 0 6 0 2z"/></svg>555 014 2290</div>
    <div><svg viewBox="0 0 10 10"><path class="ico" d="M0 2h10v6H0z"/></svg>hello@spinewell.com</div>
  </div>
  <div class="band" style="height:19px"><div class="teal"></div><div class="navy" style="width:152px;font-size:5.6px;justify-content:flex-start;padding-left:26px">www.spinewell.com</div></div>
</section>

<!-- BUSINESS CARD FRONT -->
<section class="sheet" style="left:430px;top:566px;width:139px;height:79px;background:linear-gradient(135deg,#0a9ad3,#0b8fc8)">
  <div class="brand on-blue" style="left:28px;top:33px;font-size:11px"><span class="mark" style="width:9px;height:9px"></span>SpineWell</div>
</section>

<!-- BUSINESS CARD BACK -->
<section class="sheet" style="left:584px;top:566px;width:139px;height:79px;background:linear-gradient(135deg,#fff,var(--paper-tint))">
  <div class="brand" style="right:9px;top:11px;font-size:9px"><span class="mark" style="width:7px;height:7px"></span>SpineWell</div>
  <div class="abs" style="left:10px;top:31px;font-size:6.5px;font-weight:600;color:var(--navy)">DANA MERCER</div>
  <div class="abs" style="left:10px;top:39px;font-size:4px;color:var(--blue)">DIRECTOR</div>
  <div class="contact" style="left:10px;top:53px;font-size:4px;line-height:6.3px">
    <div><svg viewBox="0 0 10 10" style="width:4px;height:4px"><path class="ico" d="M2 0l2 2-1 2c1 1 2 2 3 3l2-1 2 2-2 2C4 10 0 6 0 2z"/></svg>555 014 2290</div>
    <div><svg viewBox="0 0 10 10" style="width:4px;height:4px"><path class="ico" d="M0 2h10v6H0z"/></svg>hello@spinewell.com</div>
    <div style="font-weight:600;color:var(--navy)">www.spinewell.com</div>
  </div>
  <div class="contact" style="left:76px;top:53px;font-size:4px;line-height:6.3px"><div>1420 Orchard Ln</div><div>Fairview California 95210</div></div>
  <div class="band" style="height:5px"><div class="teal"></div><div class="navy" style="width:60px"></div></div>
</section>

<!-- ENVELOPE BACK -->
<section class="sheet" style="left:430px;top:672px;width:337px;height:165px;background:linear-gradient(135deg,#fff,var(--paper-tint))">
  <div class="brand" style="left:23px;top:35px;font-size:15px"><span class="mark" style="width:12px;height:12px"></span>SpineWell</div>
  <div class="contact" style="left:23px;top:126px">
    <div><svg viewBox="0 0 10 10"><path class="ico" d="M2 0l2 2-1 2c1 1 2 2 3 3l2-1 2 2-2 2C4 10 0 6 0 2z"/></svg>555 014 2290</div>
    <div><svg viewBox="0 0 10 10"><path class="ico" d="M0 2h10v6H0z"/></svg>hello@spinewell.com</div>
    <div style="margin-top:3px;font-weight:600;color:var(--navy)">www.spinewell.com</div>
  </div>
  <div class="contact" style="left:149px;top:126px"><div>1420 Orchard Ln</div><div>Fairview California 95210</div></div>
  <div class="band" style="height:12px"><div class="teal"></div><div class="navy" style="width:131px"></div></div>
</section>

<!-- ENVELOPE FRONT -->
<section class="sheet" style="left:430px;top:855px;width:337px;height:165px">
  <div class="abs" style="left:0;top:0;width:337px;height:38px;background:var(--navy)"></div>
  <div class="brand on-blue" style="left:0;right:0;top:9px;justify-content:center;font-size:11px"><span class="mark" style="width:9px;height:9px"></span>SpineWell</div>
  <div class="abs" style="left:0;right:0;top:25px;text-align:center;font-size:4.5px;font-weight:600;color:#fff">www.spinewell.com</div>
</section>

<!-- NOTEPAD -->
<section class="sheet" style="left:803px;top:566px;width:219px;height:337px">
  <div class="brand" style="left:14px;top:12px;font-size:10px"><span class="mark" style="width:8px;height:8px"></span>SpineWell</div>
  <div class="contact" style="left:149px;top:11px;font-size:4.5px;line-height:7.5px">
    <div><svg viewBox="0 0 10 10" style="width:4px;height:4px"><path class="ico" d="M2 0l2 2-1 2c1 1 2 2 3 3l2-1 2 2-2 2C4 10 0 6 0 2z"/></svg>555 014 2290</div>
    <div><svg viewBox="0 0 10 10" style="width:4px;height:4px"><path class="ico" d="M0 2h10v6H0z"/></svg>hello@spinewell.com</div>
  </div>
  <div class="notepad-lines">
    <div></div><div></div><div></div><div></div><div></div><div></div><div></div><div></div><div></div><div></div>
    <div></div><div></div><div></div><div></div><div></div><div></div><div></div><div></div><div></div><div></div>
    <div></div><div></div><div></div><div></div><div></div>
  </div>
  <div class="band" style="height:12px"><div class="teal"></div><div class="navy" style="width:98px;font-size:4.5px">www.spinewell.com</div></div>
</section>

</body>
</html>
```